Marrowind Labs - pioneers of next generation consulting!

We are a next generation management consulting firm with two focus areas and USPs (unique selling points):>Technology driven business developmentWe are not developers, we are experts in HOW to apply and incorporate technology in your business dna to drive business growth and value-added change.>Creating high performing teams levering our philosophy of collective intelligence. We truly understand the need of human engagement and we know that the only way of getting there is by building strong relationships among people, a warm and open culture is a stepping stone towards effective collaboration within/among teams. - We don't want a ”corporate feel” to our templates. The organic feeling we have with our blue-on-blue blobs has the idea of ever changing movement and shape changing. Please see our website, www.marrowindlabs.se. - In our context we sit among classic business mgmt. consultants and classic IT mgmt. consultants. We cater to business, tech and humans as the ultimate vehicle of change and business value. -To have a clean template one suggestion is to only use blue, white and black and keeping other colors separate, as an alternative but we are truly open allow your creativity add value to this. We are looking to find a slide deck which we can pick slides from, depending on what/whom/why we interact with customer we want to create different outcomes and our presentations should support this.

Industry/Entity Type

Management Consulting

Requirements
Must have
• next generation powerpoint and how to package storytelling. please keep to our look and feel, we just arrived at our logo, colours and shapes. Help us to carry it into our ppt's as well.
Should not have
• Hi all, please have a look at our website. It is still very new and more will be done, but our goal is to make powerpoint to come alive again and mirror our pioneering hearts and brains.

```html
<!DOCTYPE html>
<html lang="en">
<head>
<meta charset="utf-8">
<title>Marrowind Labs – Slide Deck</title>
<link href="https://fonts.googleapis.com/css2?family=Nunito+Sans:ital,wght@0,400;0,600;0,700;0,800;1,400&display=swap" rel="stylesheet">
<style>
:root{
  --bg:#eceef1;
  --navy:#173a73;
  --deep:#122d5c;
  --blue:#2a5db0;
  --mid:#3b73c4;
  --sky:#6a9be0;
  --pale:#dce6f4;
  --green:#3cae4b;
  --ink:#24324d;
  --grey:#8a93a3;
  --white:#ffffff;
}
*{box-sizing:border-box;margin:0;padding:0}
html,body{width:1200px;height:2257px;overflow:hidden}
body{background:var(--bg);font-family:"Nunito Sans",Arial,sans-serif;color:var(--ink);position:relative}
.defs{position:absolute;width:0;height:0}

/* layout */
.hero{position:absolute;left:0;top:0;width:1200px;height:660px}
.hero .slide{position:absolute;top:170px;transform:scale(1.46);transform-origin:0 0}
.hero .slide:first-child{left:45px}
.hero .slide:last-child{left:612px}
.deck{position:absolute;left:21px;top:693px;display:grid;grid-template-columns:repeat(3,373px);grid-auto-rows:208px;column-gap:19px;row-gap:14px}

/* slide base */
.slide{position:relative;width:373px;height:208px;overflow:hidden;background:var(--white);box-shadow:0 1px 3px rgba(0,0,0,.18)}
.slide--blue{background:var(--blue);color:var(--white)}
.photo{position:absolute;background:linear-gradient(135deg,#5f6b78,#2e3a4a 60%,#47505c)}
.photo--warm{background:linear-gradient(135deg,#8a7a6c,#4b4a4e 55%,#6f6660)}
.photo--tech{background:linear-gradient(135deg,#c9ced6,#7d8c9c 50%,#3d5a48)}
.photo--robot{background:linear-gradient(120deg,#1d3d7a,#6d86b3 55%,#d7dde8)}
.photo--bird{background:linear-gradient(120deg,#2a5db0 30%,#9b7a5a 70%,#5a3b2a)}
.overlay{position:absolute;inset:0;background:rgba(23,58,140,.55)}
.blob{position:absolute}

.slide-title{position:absolute;left:18px;top:14px;font-size:10.5px;font-weight:700;color:var(--navy);text-transform:uppercase;letter-spacing:.2px}
.slide--blue .slide-title{color:var(--white)}
.slide-title--center{left:0;right:0;text-align:center}
.subhead{font-size:6.5px;font-weight:700;color:var(--blue);margin-bottom:3px}
.slide--blue .subhead{color:var(--white)}
.bullets{position:absolute;left:18px;top:34px;font-size:5.2px;line-height:1.45;list-style:none}
.bullets li{padding-left:6px;position:relative}
.bullets li::before{content:"◆";position:absolute;left:0;font-size:4px;top:.5px}
.bullets li.sub{padding-left:14px;font-size:4.4px;margin-bottom:2px}
.bullets li.sub::before{left:8px}
.body{font-size:5px;line-height:1.4;color:var(--ink)}

.footer-brand{position:absolute;left:16px;bottom:8px;font-size:6px;font-weight:800;letter-spacing:.5px;color:var(--navy);text-transform:uppercase}
.slide--blue .footer-brand{color:var(--white)}
.footer-url{position:absolute;right:32px;bottom:8px;font-size:4.3px;color:var(--grey)}
.slide--blue .footer-url{color:var(--pale)}
.page{position:absolute;right:12px;bottom:6px;width:14px;height:8px;border-radius:4px;background:var(--navy);color:var(--white);font-size:4.5px;text-align:center;line-height:8px}
.slide--blue .page{background:var(--deep)}

/* title */
.brand{font-weight:800;text-transform:uppercase;letter-spacing:.6px;color:var(--white)}
.cover-text{position:absolute;left:22px;top:54px;color:var(--white)}
.cover-text .brand{font-size:11px;margin-bottom:14px}
.cover-text h1{font-size:10.5px;font-weight:800;text-transform:uppercase;line-height:1}
.cover-text h2{font-size:7px;font-weight:400;margin-bottom:12px}
.cover-text .date{font-size:6px}
.section-text{position:absolute;color:var(--white)}
.section-text h2{font-size:11px;font-weight:700;line-height:1.1}
.section-text p{font-size:6.5px;color:var(--pale)}

/* chart bits */
.chart{position:absolute}
.caption{font-size:4.5px;fill:var(--grey)}
.icon-label{font-size:5.5px;font-weight:700;color:var(--navy)}
.name{font-size:5.5px;font-weight:700;color:var(--navy);text-align:center}
.cap-text{font-size:4.5px;color:var(--grey);text-align:center;line-height:1.35}
.quote{position:absolute;left:40px;right:40px;text-align:center;font-style:italic;font-size:7px;line-height:1.45}
.tile{position:absolute;font-size:4.5px;line-height:1.35;color:var(--white);padding:5px}
.tile h3{font-size:5.5px;font-weight:700;margin-bottom:2px}
</style>
</head>
<body>

<svg class="defs" aria-hidden="true">
  <defs>
    <path id="blob" d="M44,16 C92,-8 168,8 186,66 C204,128 162,192 96,188 C32,184 -6,146 4,94 C10,56 20,30 44,16Z"/>
    <path id="blob2" d="M30,30 C70,-4 150,0 180,40 C206,80 196,150 140,180 C86,206 28,190 10,140 C-4,100 4,56 30,30Z"/>
  </defs>
</svg>

<!-- Hero pair -->
<section class="hero">
  <article class="slide slide--blue">
    <div class="photo photo--warm" style="inset:0" role="img" aria-label="Photo of a workshop audience raising hands"></div>
    <div class="overlay"></div>
    <svg class="blob" style="left:-40px;top:80px" width="150" height="150" viewBox="0 0 200 200"><use href="#blob2" fill="var(--blue)"/><use href="#blob2" fill="var(--navy)" transform="translate(20 20) scale(.8)"/></svg>
    <div class="section-text" style="left:20px;top:122px"><h2>Section Slide</h2><p>Sub Divider Presentation</p></div>
  </article>
  <article class="slide slide--blue">
    <div class="photo photo--robot" style="left:150px;top:0;right:0;bottom:0" role="img" aria-label="Photo of a humanoid service robot"></div>
    <svg class="blob" style="left:-50px;top:-40px" width="270" height="270" viewBox="0 0 200 200"><use href="#blob" fill="var(--blue)"/><use href="#blob" fill="var(--navy)" transform="translate(14 10) scale(.86)"/></svg>
    <div class="cover-text"><div class="brand">Marrowind Labs</div><h1>Presentation Title</h1><h2>Sub Presentation Title</h2><div class="date">April, 2018</div></div>
  </article>
</section>

<main class="deck">
  <!-- 1 title -->
  <article class="slide slide--blue">
    <div class="photo photo--robot" style="left:150px;top:0;right:0;bottom:0" role="img" aria-label="Photo of a humanoid service robot"></div>
    <svg class="blob" style="left:-50px;top:-40px" width="270" height="270" viewBox="0 0 200 200"><use href="#blob" fill="var(--blue)"/><use href="#blob" fill="var(--navy)" transform="translate(14 10) scale(.86)"/></svg>
    <div class="cover-text"><div class="brand">Marrowind Labs</div><h1>Presentation Title</h1><h2>Sub Presentation Title</h2><div class="date">April, 2018</div></div>
  </article>
  <!-- 2 section -->
  <article class="slide slide--blue">
    <div class="photo photo--warm" style="inset:0" role="img" aria-label="Photo of a workshop audience raising hands"></div>
    <div class="overlay"></div>
    <svg class="blob" style="left:-40px;top:80px" width="150" height="150" viewBox="0 0 200 200"><use href="#blob2" fill="var(--blue)"/><use href="#blob2" fill="var(--navy)" transform="translate(20 20) scale(.8)"/></svg>
    <div class="section-text" style="left:20px;top:122px"><h2>Section Slide</h2><p>Sub Divider Presentation</p></div>
  </article>
  <!-- 3 one column -->
  <article class="slide">
    <h2 class="slide-title">One Column</h2>
    <ul class="bullets" style="top:32px"><li class="subhead" style="padding:0">Lorem Ipsum</li>
      <li>Lorem ipsum dolor sit amet, te ullum corpora delicata duo. Rebum insolens pri eu.<br>No alia tota modus qui.</li><li class="sub">Sint brute et usu. Duo isque appareat adversarium et.</li>
      <li>Lorem ipsum dolor sit amet, te ullum corpora delicata duo. Rebum insolens pri eu.<br>No alia tota modus qui.</li><li class="sub">Sint brute et usu. Duo isque appareat adversarium et.</li>
      <li>Lorem ipsum dolor sit amet, te ullum corpora delicata duo. Rebum insolens pri eu.<br>No alia tota modus qui.</li><li class="sub">Sint brute et usu. Duo isque appareat adversarium et.</li>
    </ul>
    <div class="page">3</div>
  </article>
  <!-- 4 one column blue -->
  <article class="slide slide--blue">
    <h2 class="slide-title">One Column</h2>
    <ul class="bullets" style="top:32px"><li class="subhead" style="padding:0">Lorem Ipsum</li>
      <li>Lorem ipsum dolor sit amet, te ullum corpora delicata duo. Rebum insolens pri eu.<br>No alia tota modus qui.</li><li class="sub">Sint brute et usu. Duo isque appareat adversarium et.</li>
      <li>Lorem ipsum dolor sit amet, te ullum corpora delicata duo. Rebum insolens pri eu.<br>No alia tota modus qui.</li><li class="sub">Sint brute et usu. Duo isque appareat adversarium et.</li>
      <li>Lorem ipsum dolor sit amet, te ullum corpora delicata duo. Rebum insolens pri eu.<br>No alia tota modus qui.</li><li class="sub">Sint brute et usu. Duo isque appareat adversarium et.</li>
    </ul>
    <div class="footer-brand">Marrowind Labs</div><div class="footer-url">www.marrowindlabs.se</div><div class="page">4</div>
  </article>
  <!-- 5 left column + chart -->
  <article class="slide">
    <h2 class="slide-title">Left Column</h2>
    <ul class="bullets" style="top:32px;width:185px"><li class="subhead" style="padding:0">Lorem Ipsum</li>
      <li>Lorem ipsum dolor sit amet, te ullum corpora delicata duo. Rebum insolens pri eu. No alia tota modus qui.</li><li class="sub">Sint brute et usu. Duo isque appareat adversarium et.</li>
      <li>Lorem ipsum dolor sit amet, te ullum corpora delicata duo. Rebum insolens pri eu. No alia tota modus qui.</li><li class="sub">Sint brute et usu. Duo isque appareat adversarium et.</li>
      <li>Lorem ipsum dolor sit amet, te ullum corpora delicata duo. Rebum insolens pri eu. No alia tota modus qui.</li><li class="sub">Sint brute et usu. Duo isque appareat adversarium et.</li>
    </ul>
    <svg class="chart" style="left:205px;top:28px" width="155" height="150" viewBox="0 0 155 150">
      <text x="78" y="10" text-anchor="middle" class="caption" style="font-size:6px">Bar Chart Sample</text>
      <g stroke="#dfe3ea" stroke-width=".5"><line x1="14" y1="130" x2="150" y2="130"/><line x1="14" y1="100" x2="150" y2="100"/><line x1="14" y1="70" x2="150" y2="70"/><line x1="14" y1="40" x2="150" y2="40"/></g>
      <rect x="22" y="45" width="8" height="85" fill="var(--navy)"/><rect x="32" y="80" width="8" height="50" fill="var(--blue)"/><rect x="42" y="88" width="8" height="42" fill="var(--sky)"/>
      <rect x="64" y="78" width="8" height="52" fill="var(--navy)"/><rect x="74" y="40" width="8" height="90" fill="var(--blue)"/><rect x="84" y="70" width="8" height="60" fill="var(--sky)"/>
      <rect x="106" y="58" width="8" height="72" fill="var(--navy)"/><rect x="116" y="85" width="8" height="45" fill="var(--blue)"/><rect x="126" y="50" width="8" height="80" fill="var(--sky)"/>
      <text x="36" y="138" text-anchor="middle" class="caption">Category 1</text><text x="78" y="138" text-anchor="middle" class="caption">Category 2</text><text x="120" y="138" text-anchor="middle" class="caption">Category 3</text>
      <circle cx="55" cy="146" r="1.5" fill="var(--navy)"/><circle cx="75" cy="146" r="1.5" fill="var(--blue)"/><circle cx="95" cy="146" r="1.5" fill="var(--sky)"/>
    </svg>
    <div class="footer-brand">Marrowind Labs</div><div class="footer-url">www.marrowindlabs.se</div><div class="page">5</div>
  </article>
  <!-- 6 image + left column -->
  <article class="slide">
    <div class="photo photo--tech" style="left:0;top:0;width:186px;bottom:0" role="img" aria-label="Photo of hands working on circuit boards"></div>
    <h2 class="slide-title" style="left:198px">Left Column</h2>
    <ul class="bullets" style="left:198px;top:32px;width:165px"><li class="subhead" style="padding:0">Lorem Ipsum</li>
      <li>Lorem ipsum dolor sit amet, te ullum corpora delicata duo. Rebum insolens pri eu. No alia tota modus qui.</li><li class="sub">Sint brute et usu. Duo isque appareat adversarium et.</li>
      <li>Lorem ipsum dolor sit amet, te ullum corpora delicata duo. Rebum insolens pri eu. No alia tota modus qui.</li><li class="sub">Sint brute et usu. Duo isque appareat adversarium et.</li>
      <li>Lorem ipsum dolor sit amet, te ullum corpora delicata duo. Rebum insolens pri eu. No alia tota modus qui.</li><li class="sub">Sint brute et usu. Duo isque appareat adversarium et.</li>
    </ul>
    <div class="footer-url">www.marrowindlabs.se</div><div class="page">6</div>
  </article>
  <!-- 7 full photo -->
  <article class="slide slide--blue">
    <div class="photo photo--warm" style="inset:0" role="img" aria-label="Photo of a group of colleagues taking a selfie"></div>
    <div class="footer-brand">Marrowind Labs</div><div class="footer-url">www.marrowindlabs.se</div><div class="page">7</div>
  </article>
  <!-- 8 section variant -->
  <article class="slide slide--blue">
    <div class="photo" style="inset:0" role="img" aria-label="Photo of two colleagues in conversation"></div>
    <div class="overlay" style="background:rgba(23,58,140,.4)"></div>
    <svg class="blob" style="left:240px;top:90px" width="150" height="140" viewBox="0 0 200 200"><use href="#blob2" fill="var(--blue)"/><use href="#blob2" fill="var(--navy)" transform="translate(20 20) scale(.8)"/></svg>
    <div class="section-text" style="left:262px;top:128px"><h2>Section Slide</h2><p>Sub Divider Presentation</p></div>
  </article>
  <!-- 9 testimonial -->
  <article class="slide slide--blue">
    <svg class="blob" style="left:-40px;top:-60px;opacity:.35" width="160" height="160" viewBox="0 0 200 200"><use href="#blob" fill="var(--mid)"/></svg>
    <svg class="blob" style="left:280px;top:120px;opacity:.35" width="140" height="140" viewBox="0 0 200 200"><use href="#blob2" fill="var(--mid)"/></svg>
    <div class="photo" style="left:175px;top:22px;width:24px;height:28px;border-radius:50%;background:linear-gradient(#3a4f73,#1a2a48)" role="img" aria-label="Portrait photo of the quoted person"></div>
    <div style="position:absolute;left:0;right:0;top:54px;text-align:center;font-size:6px;font-weight:700">JOHN DOE</div>
    <div style="position:absolute;left:0;right:0;top:62px;text-align:center;font-size:5px;color:var(--pale)">Lorem ipsum dolor sit amet, consectetur adipiscing elit</div>
    <p class="quote" style="top:74px;font-size:5.5px;left:50px;right:50px">Lorem Ipsum is simply dummy text of the printing and industry. Lorem Ipsum has been the industry's standard dummy text ever since the 1500s, when an unknown printer took a galley of type and scrambled it to make a type specimen book.</p>
    <div style="position:absolute;right:60px;top:120px;font-size:5px;font-style:italic">- John Doe</div>
    <div class="footer-brand">Marrowind Labs</div><div class="page">9</div>
  </article>
  <!-- 10 quote -->
  <article class="slide slide--blue">
    <svg class="blob" style="left:250px;top:-50px;opacity:.3" width="160" height="160" viewBox="0 0 200 200"><use href="#blob" fill="var(--mid)"/></svg>
    <svg class="chart" style="left:60px;top:50px" width="253" height="14" viewBox="0 0 253 14"><line x1="0" y1="7" x2="110" y2="7" stroke="var(--pale)" stroke-width=".6"/><line x1="143" y1="7" x2="253" y2="7" stroke="var(--pale)" stroke-width=".6"/><circle cx="126.5" cy="7" r="6" fill="var(--white)"/><text x="126.5" y="10.5" text-anchor="middle" font-size="9" font-weight="800" fill="var(--blue)">“</text></svg>
    <p class="quote" style="top:76px">Lorem ipsum dolor sit amet, te ullum corpora delicata duo. Rebum insolens pri eu. No alia tota modus qui.</p>
    <div style="position:absolute;left:0;right:0;top:112px;text-align:center;font-size:5px">- John Doe</div>
    <svg class="chart" style="left:120px;top:126px" width="133" height="2"><line x1="0" y1="1" x2="133" y2="1" stroke="var(--pale)" stroke-width=".6"/></svg>
    <div class="footer-brand">Marrowind Labs</div><div class="page">10</div>
  </article>
  <!-- 11 content with icons -->
  <article class="slide">
    <h2 class="slide-title">Content With Icons</h2>
    <svg class="chart" style="left:40px;top:32px" width="300" height="140" viewBox="0 0 300 140">
      <g fill="var(--navy)">
        <use href="#blob" transform="translate(85 4) scale(.11)"/><use href="#blob" transform="translate(85 50) scale(.11)"/><use href="#blob" transform="translate(85 96) scale(.11)"/>
        <use href="#blob" transform="translate(155 4) scale(.11)"/><use href="#blob" transform="translate(155 50) scale(.11)"/><use href="#blob" transform="translate(155 96) scale(.11)"/>
      </g>
      <g fill="none" stroke="#fff" stroke-width="1.2">
        <circle cx="96" cy="15" r="4"/><rect x="92" y="57" width="8" height="8"/><path d="M92,111 l4,-5 l4,5z"/>
        <path d="M162,16 h10 M167,11 v10"/><path d="M162,66 l4,-4 l3,3 l4,-5"/><circle cx="166" cy="107" r="4"/>
      </g>
      <g font-size="5.5" font-weight="700" fill="var(--navy)">
        <text x="80" y="12" text-anchor="end">HEADING 1</text><text x="80" y="58" text-anchor="end">HEADING 2</text><text x="80" y="104" text-anchor="end">HEADING 3</text>
        <text x="182" y="12">HEADING 4</text><text x="182" y="58">HEADING 5</text><text x="182" y="104">HEADING 6</text>
      </g>
      <g font-size="4.3" fill="var(--grey)">
        <text x="80" y="20" text-anchor="end">Lorem ipsum dolor sit amet,</text><text x="80" y="25" text-anchor="end">consectetur adipiscing elit</text>
        <text x="80" y="66" text-anchor="end">Lorem ipsum dolor sit amet,</text><text x="80" y="71" text-anchor="end">consectetur adipiscing elit</text>
        <text x="80" y="112" text-anchor="end">Lorem ipsum dolor sit amet,</text><text x="80" y="117" text-anchor="end">consectetur adipiscing elit</text>
        <text x="182" y="20">Lorem ipsum dolor sit amet,</text><text x="182" y="25">consectetur adipiscing elit</text>
        <text x="182" y="66">Lorem ipsum dolor sit amet,</text><text x="182" y="71">consectetur adipiscing elit</text>
        <text x="182" y="112">Lorem ipsum dolor sit amet,</text><text x="182" y="117">consectetur adipiscing elit</text>
      </g>
    </svg>
    <div class="footer-brand">Marrowind Labs</div><div class="footer-url">www.marrowindlabs.se</div><div class="page">11</div>
  </article>
  <!-- 12 three circles -->
  <article class="slide">
    <h2 class="slide-title">The “3 Circles” Slide</h2>
    <svg class="chart" style="left:66px;top:30px" width="240" height="90" viewBox="0 0 240 90">
      <circle cx="55" cy="45" r="43" fill="var(--navy)" opacity=".85"/>
      <circle cx="120" cy="45" r="43" fill="var(--sky)" opacity=".85"/>
      <circle cx="185" cy="45" r="43" fill="var(--deep)" opacity=".85"/>
      <g font-size="5.5" font-weight="700" fill="#fff" text-anchor="middle"><text x="50" y="64">CULTURE</text><text x="120" y="62">BUSINESS</text><text x="120" y="69">INTENT</text><text x="190" y="64">TECHNOLOGY</text></g>
      <g fill="none" stroke="#fff" stroke-width="1.3"><path d="M44,42 h12 v-8 h-12z"/><circle cx="120" cy="40" r="6"/><path d="M184,44 l4,-5 l4,3 l5,-7"/></g>
      <g fill="#fff"><circle cx="89" cy="45" r="5"/><circle cx="151" cy="45" r="5"/></g>
      <g fill="none" stroke="var(--navy)" stroke-width="1.2"><path d="M88,42 l2,3 l-2,3"/><path d="M152,42 l-2,3 l2,3"/></g>
    </svg>
    <div class="body" style="position:absolute;left:20px;top:130px;width:100px;text-align:center">Lorem ipsum dolor sit amet, te ullum corpora delicata duo. Rebum insolens pri eu. No alia tota modus qui.</div>
    <div class="body" style="position:absolute;left:136px;top:130px;width:100px;text-align:center">Lorem ipsum dolor sit amet, te ullum corpora delicata duo. Rebum insolens pri eu. No alia tota modus qui.</div>
    <div class="body" style="position:absolute;left:252px;top:130px;width:100px;text-align:center">Lorem ipsum dolor sit amet, te ullum corpora delicata duo. Rebum insolens pri eu. No alia tota modus qui.</div>
    <div class="footer-brand">Marrowind Labs</div><div class="footer-url">www.marrowindlabs.se</div><div class="page">12</div>
  </article>
  <!-- 13 consultants -->
  <article class="slide">
    <h2 class="slide-title">Our Consultants</h2>
    <svg class="chart" style="left:20px;top:32px" width="340" height="60" viewBox="0 0 340 60">
      <g fill="var(--blue)"><use href="#blob" transform="translate(22 4) scale(.27)"/><use href="#blob" transform="translate(107 4) scale(.27)"/><use href="#blob" transform="translate(192 4) scale(.27)"/><use href="#blob" transform="translate(277 4) scale(.27)"/></g>
    </svg>
    <div class="photo" style="left:56px;top:34px;width:24px;height:58px;border-radius:10px 10px 0 0" role="img" aria-label="Portrait photo of Milo Harwick"></div>
    <div class="photo" style="left:141px;top:34px;width:24px;height:58px;border-radius:10px 10px 0 0" role="img" aria-label="Portrait photo of Edda Brenner"></div>
    <div class="photo" style="left:226px;top:34px;width:24px;height:58px;border-radius:10px 10px 0 0" role="img" aria-label="Portrait photo of Tomas Vellacott"></div>
    <div class="photo" style="left:311px;top:34px;width:24px;height:58px;border-radius:10px 10px 0 0" role="img" aria-label="Portrait photo of Ines Aldercroft"></div>
    <div style="position:absolute;left:20px;top:96px;width:340px;display:grid;grid-template-columns:repeat(4,85px)">
      <div><div class="name">Milo Harwick</div><div class="cap-text">Lorem ipsum dolor sit<br>amet, consectetur<br>adipiscing elit</div></div>
      <div><div class="name">Edda Brenner</div><div class="cap-text">Lorem ipsum dolor sit<br>amet, consectetur<br>adipiscing elit</div></div>
      <div><div class="name">Tomas Vellacott</div><div class="cap-text">Lorem ipsum dolor sit<br>amet, consectetur<br>adipiscing elit</div></div>
      <div><div class="name">Ines Aldercroft</div><div class="cap-text">Lorem ipsum dolor sit<br>amet, consectetur<br>adipiscing elit</div></div>
    </div>
    <div class="footer-brand">Marrowind Labs</div><div class="footer-url">www.marrowindlabs.se</div><div class="page">13</div>
  </article>
  <!-- 14 graph -->
  <article class="slide">
    <h2 class="slide-title">Graph Slides Sample</h2>
    <svg class="chart" style="left:146px;top:34px" width="82" height="82" viewBox="0 0 82 82">
      <g fill="none" stroke-width="18" transform="rotate(-90 41 41)">
        <circle cx="41" cy="41" r="31" pathLength="100" stroke="var(--navy)" stroke-dasharray="11.5 88.5" stroke-dashoffset="0"/>
        <circle cx="41" cy="41" r="31" pathLength="100" stroke="var(--blue)" stroke-dasharray="11.5 88.5" stroke-dashoffset="-12.5"/>
        <circle cx="41" cy="41" r="31" pathLength="100" stroke="var(--navy)" stroke-dasharray="11.5 88.5" stroke-dashoffset="-25"/>
        <circle cx="41" cy="41" r="31" pathLength="100" stroke="var(--blue)" stroke-dasharray="11.5 88.5" stroke-dashoffset="-37.5"/>
        <circle cx="41" cy="41" r="31" pathLength="100" stroke="var(--navy)" stroke-dasharray="11.5 88.5" stroke-dashoffset="-50"/>
        <circle cx="41" cy="41" r="31" pathLength="100" stroke="var(--blue)" stroke-dasharray="11.5 88.5" stroke-dashoffset="-62.5"/>
        <circle cx="41" cy="41" r="31" pathLength="100" stroke="var(--navy)" stroke-dasharray="11.5 88.5" stroke-dashoffset="-75"/>
        <circle cx="41" cy="41" r="31" pathLength="100" stroke="var(--blue)" stroke-dasharray="11.5 88.5" stroke-dashoffset="-87.5"/>
      </g>
      <text x="41" y="40" text-anchor="middle" font-size="5.5" font-weight="800" fill="var(--navy)">MARROWIND</text>
      <text x="41" y="47" text-anchor="middle" font-size="5.5" font-weight="800" fill="var(--navy)">LABS</text>
    </svg>
    <div class="cap-text" style="position:absolute;left:40px;top:40px;width:90px;text-align:right">Lorem ipsum dolor sit amet,<br>consectetur adipiscing elit</div>
    <div class="cap-text" style="position:absolute;left:40px;top:70px;width:90px;text-align:right">Lorem ipsum dolor sit amet,<br>consectetur adipiscing elit</div>
    <div class="cap-text" style="position:absolute;left:40px;top:100px;width:90px;text-align:right">Lorem ipsum dolor sit amet,<br>consectetur adipiscing elit</div>
    <div class="cap-text" style="position:absolute;left:244px;top:40px;width:90px;text-align:left">Lorem ipsum dolor sit amet,<br>consectetur adipiscing elit</div>
    <div class="cap-text" style="position:absolute;left:244px;top:70px;width:90px;text-align:left">Lorem ipsum dolor sit amet,<br>consectetur adipiscing elit</div>
    <div class="cap-text" style="position:absolute;left:244px;top:100px;width:90px;text-align:left">Lorem ipsum dolor sit amet,<br>consectetur adipiscing elit</div>
    <div class="footer-brand">Marrowind Labs</div><div class="footer-url">www.marrowindlabs.se</div><div class="page">14</div>
  </article>
  <!-- 15 data -->
  <article class="slide">
    <h2 class="slide-title">Data Sample</h2>
    <svg class="chart" style="left:30px;top:30px" width="313" height="56" viewBox="0 0 313 56">
      <g fill="none" stroke-width="4" transform="translate(30 2)">
        <circle cx="26" cy="26" r="22" stroke="#e3e8f0"/><circle cx="26" cy="26" r="22" pathLength="100" stroke="var(--navy)" stroke-dasharray="25 75" transform="rotate(-90 26 26)"/>
        <circle cx="130" cy="26" r="22" stroke="#e3e8f0"/><circle cx="130" cy="26" r="22" pathLength="100" stroke="var(--blue)" stroke-dasharray="47 53" transform="rotate(-90 130 26)"/>
        <circle cx="234" cy="26" r="22" stroke="#e3e8f0"/><circle cx="234" cy="26" r="22" pathLength="100" stroke="var(--mid)" stroke-dasharray="70 30" transform="rotate(-90 234 26)"/>
      </g>
      <g font-size="8" font-weight="800" fill="var(--ink)" text-anchor="middle"><text x="56" y="31">25%</text><text x="160" y="31">47%</text><text x="264" y="31">70%</text></g>
    </svg>
    <div style="position:absolute;left:30px;top:92px;width:313px;display:grid;grid-template-columns:repeat(3,104px)">
      <div><div class="name" style="color:var(--blue)">LOREM IPSUM</div><div class="cap-text">Lorem ipsum dolor sit amet,<br>te ullum corpora delicata duo.<br>Rebum insolens pri eu.<br>No alia<br>tota modus qui.</div></div>
      <div><div class="name" style="color:var(--blue)">LOREM IPSUM</div><div class="cap-text">Lorem ipsum dolor sit amet,<br>te ullum corpora delicata duo.<br>Rebum insolens pri eu.<br>No alia<br>tota modus qui.</div></div>
      <div><div class="name" style="color:var(--blue)">LOREM IPSUM</div><div class="cap-text">Lorem ipsum dolor sit amet,<br>te ullum corpora delicata duo.<br>Rebum insolens pri eu.<br>No alia<br>tota modus qui.</div></div>
    </div>
    <div class="footer-brand">Marrowind Labs</div><div class="footer-url">www.marrowindlabs.se</div><div class="page">15</div>
  </article>
  <!-- 16 timeline -->
  <article class="slide">
    <h2 class="slide-title">Timeline Sample</h2>
    <svg class="chart" style="left:20px;top:30px" width="340" height="140" viewBox="0 0 340 140">
      <g font-size="4.3" fill="var(--grey)">
        <text x="45" y="10">Lorem ipsum dolor sit</text><text x="45" y="15">amet, consectetur</text><text x="45" y="20">adipiscing elit</text>
        <text x="140" y="10">Lorem ipsum dolor sit</text><text x="140" y="15">amet, consectetur</text><text x="140" y="20">adipiscing elit</text>
        <text x="235" y="10">Lorem ipsum dolor sit</text><text x="235" y="15">amet, consectetur</text><text x="235" y="20">adipiscing elit</text>
        <text x="92" y="112">Lorem ipsum dolor sit</text><text x="92" y="117">amet, consectetur</text><text x="92" y="122">adipiscing elit</text>
        <text x="187" y="112">Lorem ipsum dolor sit</text><text x="187" y="117">amet, consectetur</text><text x="187" y="122">adipiscing elit</text>
        <text x="282" y="112">Lorem ipsum dolor sit</text><text x="282" y="117">amet, consectetur</text><text x="282" y="122">adipiscing elit</text>
      </g>
      <g stroke="var(--grey)" stroke-width=".4" stroke-dasharray="1 1"><line x1="58" y1="24" x2="58" y2="50"/><line x1="153" y1="24" x2="153" y2="50"/><line x1="248" y1="24" x2="248" y2="50"/><line x1="105" y1="80" x2="105" y2="106"/><line x1="200" y1="80" x2="200" y2="106"/><line x1="295" y1="80" x2="295" y2="106"/></g>
      <g fill="var(--mid)"><circle cx="58" cy="52" r="4"/><circle cx="153" cy="52" r="4"/><circle cx="248" cy="52" r="4"/><circle cx="105" cy="78" r="4"/><circle cx="200" cy="78" r="4"/><circle cx="295" cy="78" r="4"/></g>
      <g>
        <polygon points="36,58 76,58 72,72 32,72" fill="var(--navy)"/><polygon points="80,58 120,58 116,72 76,72" fill="var(--blue)"/>
        <polygon points="124,58 164,58 160,72 120,72" fill="var(--navy)"/><polygon points="168,58 208,58 204,72 164,72" fill="var(--blue)"/>
        <polygon points="212,58 252,58 248,72 208,72" fill="var(--navy)"/><polygon points="256,58 296,58 292,72 252,72" fill="var(--blue)"/>
      </g>
      <g font-size="6.5" font-weight="700" fill="#fff" text-anchor="middle"><text x="54" y="67.5">2010</text><text x="98" y="67.5">2011</text><text x="142" y="67.5">2012</text><text x="186" y="67.5">2013</text><text x="230" y="67.5">2014</text><text x="274" y="67.5">2015</text></g>
    </svg>
    <div class="footer-brand">Marrowind Labs</div><div class="footer-url">www.marrowindlabs.se</div><div class="page">16</div>
  </article>
  <!-- 17 icons on wave -->
  <article class="slide">
    <svg class="chart" style="left:0;top:0" width="373" height="90" viewBox="0 0 373 90" preserveAspectRatio="none"><path d="M0,0 H373 V62 C300,40 250,70 190,78 C120,88 60,58 0,70Z" fill="var(--blue)"/></svg>
    <h2 class="slide-title slide-title--center" style="color:#fff">Content With Icons</h2>
    <p style="position:absolute;left:80px;right:80px;top:30px;text-align:center;font-size:5.5px;font-style:italic;color:#fff;font-weight:600">Lorem ipsum dolor sit amet, te ullum corpora delicata duo. Rebum insolens pri eu. No alia tota modus qui.</p>
    <svg class="chart" style="left:0;top:58px" width="373" height="40" viewBox="0 0 373 40">
      <circle cx="72" cy="16" r="8" fill="var(--navy)" stroke="#fff" stroke-width="1.5"/><circle cx="185" cy="26" r="8" fill="var(--blue)" stroke="#fff" stroke-width="1.5"/><circle cx="298" cy="10" r="8" fill="var(--green)" stroke="#fff" stroke-width="1.5"/>
      <g fill="none" stroke="#fff" stroke-width="1"><path d="M69,18 h6 M72,13 v6"/><rect x="182" y="23" width="6" height="6"/><path d="M295,11 l2,2 l4,-4"/></g>
    </svg>
    <div style="position:absolute;left:40px;top:100px;width:90px"><div class="icon-label">HEADING 1</div><div class="body">Lorem ipsum dolor sit amet, consectetur adipiscing elit</div></div>
    <div style="position:absolute;left:160px;top:108px;width:90px"><div class="icon-label">HEADING 2</div><div class="body">Lorem ipsum dolor sit amet, consectetur adipiscing elit</div></div>
    <div style="position:absolute;left:268px;top:94px;width:90px"><div class="icon-label" style="color:var(--green)">HEADING 3</div><div class="body">Lorem ipsum dolor sit amet, consectetur adipiscing elit</div></div>
    <div class="footer-brand">Marrowind Labs</div><div class="footer-url">www.marrowindlabs.se</div><div class="page">17</div>
  </article>
  <!-- 18 chart -->
  <article class="slide">
    <h2 class="slide-title">Chart Sample</h2>
    <svg class="chart" style="left:30px;top:28px" width="320" height="155" viewBox="0 0 320 155">
      <text x="165" y="8" text-anchor="middle" class="caption" style="font-size:5.5px">LOREM IPSUM DOLOR SIT AMET</text>
      <g stroke="#e3e7ee" stroke-width=".5"><line x1="14" y1="130" x2="318" y2="130"/><line x1="14" y1="105" x2="318" y2="105"/><line x1="14" y1="80" x2="318" y2="80"/><line x1="14" y1="55" x2="318" y2="55"/><line x1="14" y1="30" x2="318" y2="30"/></g>
      <rect x="24" y="66" width="10" height="64" fill="var(--navy)"/><rect x="57" y="94" width="10" height="36" fill="var(--blue)"/><rect x="90" y="78" width="10" height="52" fill="var(--green)"/>
      <rect x="123" y="62" width="10" height="68" fill="var(--blue)"/><rect x="156" y="94" width="10" height="36" fill="var(--navy)"/><rect x="189" y="106" width="10" height="24" fill="var(--green)"/>
      <rect x="222" y="46" width="10" height="84" fill="var(--navy)"/><rect x="255" y="84" width="10" height="46" fill="var(--blue)"/><rect x="288" y="72" width="10" height="58" fill="var(--navy)"/>
      <g class="caption" style="font-size:3.5px" text-anchor="middle"><text x="29" y="137">Category 1</text><text x="62" y="137">Category 2</text><text x="95" y="137">Category 3</text><text x="128" y="137">Category 4</text><text x="161" y="137">Category 5</text><text x="194" y="137">Category 6</text><text x="227" y="137">Category 7</text><text x="260" y="137">Category 8</text><text x="293" y="137">Category 9</text></g>
    </svg>
    <div class="page">18</div>
  </article>
  <!-- 19 content with image -->
  <article class="slide">
    <h2 class="slide-title">Content With Image</h2>
    <div class="photo photo--warm" style="left:0;top:36px;width:125px;height:58px" role="img" aria-label="Photo of a team meeting around a table"></div>
    <div class="tile" style="left:125px;top:36px;width:124px;height:58px;background:var(--navy);text-align:center;padding-top:10px"><h3>HEADING 2</h3>Lorem ipsum dolor sit amet,<br>consectetur adipiscing elit</div>
    <div class="photo" style="left:249px;top:36px;width:124px;height:58px" role="img" aria-label="Photo of colleagues talking in an office"></div>
    <div class="tile" style="left:0;top:94px;width:125px;height:58px;background:var(--deep);text-align:center;padding-top:10px"><h3>HEADING 1</h3>Lorem ipsum dolor sit amet,<br>consectetur adipiscing elit</div>
    <div class="photo photo--tech" style="left:125px;top:94px;width:124px;height:58px" role="img" aria-label="Photo of people collaborating at a desk"></div>
    <div class="tile" style="left:249px;top:94px;width:124px;height:58px;background:var(--blue);text-align:center;padding-top:10px"><h3>HEADING 3</h3>Lorem ipsum dolor sit amet,<br>consectetur adipiscing elit</div>
    <div class="footer-brand">Marrowind Labs</div><div class="footer-url">www.marrowindlabs.se</div><div class="page">19</div>
  </article>
  <!-- 20 collaboration pics -->
  <article class="slide">
    <h2 class="slide-title">Collaboration Pics</h2>
    <div class="photo photo--warm" style="left:14px;top:34px;width:42px;height:40px" role="img" aria-label="Photo of a team discussion"></div>
    <div class="tile" style="left:58px;top:34px;width:42px;height:40px;background:var(--navy)"><h3>Heading Sample</h3>Lorem ipsum dolor sit amet.</div>
    <div class="photo" style="left:102px;top:34px;width:42px;height:40px" role="img" aria-label="Photo of a workshop"></div>
    <div class="tile" style="left:146px;top:34px;width:42px;height:40px;background:var(--blue)"><h3>Heading Sample</h3>Lorem ipsum dolor sit amet.</div>
    <div class="tile" style="left:190px;top:34px;width:42px;height:40px;background:var(--green)"><h3>Heading Sample</h3>Lorem ipsum dolor sit amet.</div>
    <div class="photo photo--tech" style="left:234px;top:34px;width:42px;height:40px" role="img" aria-label="Photo of a laptop on a desk"></div>
    <div class="tile" style="left:278px;top:34px;width:42px;height:40px;background:var(--navy)"><h3>Heading Sample</h3>Lorem ipsum dolor sit amet.</div>
    <div class="tile" style="left:14px;top:78px;width:42px;height:40px;background:var(--blue)"><h3>Heading Sample</h3>Lorem ipsum dolor sit amet.</div>
    <div class="photo photo--tech" style="left:58px;top:78px;width:42px;height:40px" role="img" aria-label="Photo of people working at computers"></div>
    <div class="tile" style="left:102px;top:78px;width:42px;height:40px;background:var(--navy)"><h3>Heading Sample</h3>Lorem ipsum dolor sit amet.</div>
    <div class="photo photo--warm" style="left:146px;top:78px;width:42px;height:40px" role="img" aria-label="Photo of a colleague portrait"></div>
    <div class="tile" style="left:190px;top:78px;width:42px;height:40px;background:var(--blue)"><h3>Heading Sample</h3>Lorem ipsum dolor sit amet.</div>
    <div class="photo" style="left:234px;top:78px;width:42px;height:40px" role="img" aria-label="Photo of a meeting room"></div>
    <div class="tile" style="left:278px;top:78px;width:42px;height:40px;background:var(--navy)"><h3>Heading Sample</h3>Lorem ipsum dolor sit amet.</div>
    <div class="page">20</div>
  </article>
  <!-- 21 thank you -->
  <article class="slide slide--blue">
    <div class="photo photo--bird" style="left:160px;top:0;right:0;bottom:0" role="img" aria-label="Photo of a rooster standing indoors"></div>
    <svg class="blob" style="left:-60px;top:-30px" width="280" height="270" viewBox="0 0 200 200"><use href="#blob" fill="var(--blue)"/><use href="#blob" fill="var(--navy)" transform="translate(14 10) scale(.86)"/></svg>
    <div class="cover-text" style="top:80px"><div class="brand">Marrowind Labs</div><h1 style="font-size:12px">Thank You</h1></div>
    <div style="position:absolute;left:22px;bottom:14px;font-size:5px;color:var(--pale)">www.marrowindlabs.se</div>
  </article>
</main>
</body>
</html>
```